Revise my existing consulting brief with new logo

I just got a logo from Pixel Harbor for my new management consulting business, and would like to add it to my existing consulting brief, both 1 and 2 page versions, and would like to improve the layout of these documents to make them look more professional. These documents are essentially the brochure or flyer for my business, so they need to be easy to read and understand quickly. I would like these to be either ppt or Word format so that I can update wording in future, and so that I can save to pdf when I want to share with prospective clients. My new logo print file is attached here, as well as the consulting brief documents that need new layout.
Colors and layout used in the revised consulting brief that you will produce should be aligned to the new logo
Updates

Many of you proposed designs that took into account just one of the 2 documents I sent. However, please be advised that I am looking for designs for both documents that I sent, which are 1- and 2-paged versions of my consulting brief, which is essentially a flyer or brochure that explains my consulting service.

This should not look like a resume, but should be more attractive as a kind of business flyer/brochure.

Please also be aware that I am open to landscape format designs, not just portrait, which would be more in line with the versions I sent you.

Target Market(s)

Pharmaceutical and medical device companies

Industry/Entity Type

Pharmaceutical and medical device

Font styles to use
Serif
Sans Serif

Requirements
Must have
• Color and look that align to my new logo. Ability for me to update the text later on my own as needed, so that I can adapt it to different clients.
Should not have
• I am not looking for a PowerPoint template or stationary to match my logo. I am just looking to have the consulting briefs that I sent revised so that they fit the new logo and look more professional in layout.

```html
<!DOCTYPE html>
<html lang="en">
<head>
<meta charset="utf-8">
<title>Claire Moreau – Consulting Brief</title>
<link href="https://fonts.googleapis.com/css2?family=Carlito:ital,wght@0,400;0,700&family=Poppins:wght@400;600;700&display=swap" rel="stylesheet">
<style>
  :root{
    --navy:#1b3a8c;
    --teal:#22c2c4;
    --ink:#1e1e1e;
    --rule:#b9b9b9;
    --shade:#efeff0;
    --canvas:#b3b3b3;
    --paper:#ffffff;
  }
  *{box-sizing:border-box;margin:0;padding:0}
  html,body{width:1200px;height:841px;overflow:hidden;background:var(--canvas)}
  body{position:relative;font-family:"Carlito",Calibri,sans-serif;color:var(--ink)}
  .page{position:absolute;width:516px;height:727px;background:var(--paper);overflow:hidden}
  .page--one{left:53px;top:53px}
  .page--two{left:624px;top:51px}

  .brand{position:absolute;left:48px;top:22px;display:flex;align-items:center;gap:6px}
  .brand__mark{width:16px;height:16px;border-radius:50%;background:var(--navy)}
  .brand__name{font-family:"Poppins",sans-serif;font-weight:700;color:var(--navy);font-size:15px;line-height:15px;letter-spacing:.3px}
  .brand__name span{display:block}

  .identity{position:absolute;left:261px;top:12px}
  .identity__name{font-family:"Poppins",sans-serif;font-weight:700;color:var(--navy);font-size:19px;line-height:22px}
  .identity__role{display:inline-block;background:var(--teal);color:#fff;font-family:"Poppins",sans-serif;font-weight:600;font-size:10.5px;line-height:12px;padding:0 3px;margin-top:1px;letter-spacing:.2px}
  .identity__claims{list-style:none;margin-top:4px;font-family:"Poppins",sans-serif;color:var(--navy);font-size:11px;line-height:12px}
  .identity__claims li::before{content:"☑ ";font-size:10px}

  .contact-band{position:absolute;left:0;top:92px;width:516px;height:25px}
  .contact-band svg{position:absolute;left:0;top:0}
  .contact-list{position:absolute;left:128px;top:0;height:25px;display:flex;align-items:center;gap:5px;font-family:"Poppins",sans-serif;color:#fff;font-size:8px;white-space:nowrap}
  .contact-list .strong{font-weight:700}
  .ico{display:inline-block;vertical-align:middle}

  .foot-band{position:absolute;left:0;bottom:0;width:516px;height:12px}

  .copy{position:absolute;left:47px;width:424px;font-size:9.4px;line-height:14.6px;text-align:justify}
  .lead-name{font-variant:small-caps;color:var(--navy);font-size:10.5px;letter-spacing:.4px}
  .section-title{position:absolute;left:47px;font-variant:small-caps;color:var(--navy);font-size:11px;letter-spacing:.5px}

  .capabilities{position:absolute;left:42px;top:234px;width:432px;border-collapse:collapse;font-size:9.2px;line-height:12.7px}
  .capabilities td{border:1px solid var(--rule);vertical-align:top;padding:4px 4px 1px}
  .capabilities tr:nth-child(2) td{background:var(--shade)}
  .capabilities .area{width:117px;font-weight:700}
  .capabilities ul{padding-left:36px}
  .capabilities .emph{font-weight:700}

  .about-title{position:absolute;left:47px;top:134px;color:var(--navy);font-size:10px;letter-spacing:.6px}
  .portrait{position:absolute;left:47px;top:158px;width:88px;height:88px;background:linear-gradient(160deg,#8a8a86,#5c5a4c 60%,#4b4a36)}
  .about-intro{position:absolute;left:142px;top:156px;width:329px;font-size:9.2px;line-height:13.9px;text-align:justify}
  .about-more{position:absolute;left:47px;top:255px;width:424px;font-size:9.2px;line-height:13.9px;text-align:justify}
  .about-more p{margin-bottom:8.5px}

  .achievements{position:absolute;left:45px;top:393px;width:426px;height:277px;background:var(--shade);padding:0 1px 0 2px}
  .achievements__title{color:var(--navy);font-size:10px;line-height:11.5px;letter-spacing:.6px;padding-top:1px}
  .achievements ul{list-style:square;padding-left:16px;margin-top:5px;font-size:9.2px;line-height:12.8px;text-align:justify}
  .achievements li{margin-bottom:5px;padding-left:0}
  .achievements .key{color:#000}
</style>
</head>
<body>

<!-- Page 1 -->
<section class="page page--one">
  <div class="brand"><span class="brand__mark"></span><div class="brand__name"><span>NORTHBOUND</span><span>ADVISORY LLC</span></div></div>
  <div class="identity">
    <div class="identity__name">Claire Moreau</div>
    <div class="identity__role">INDEPENDENT CONSULTANT</div>
    <ul class="identity__claims"><li>Solving Complex Challenges</li><li>Driving Programs from Strategy to Action</li></ul>
  </div>
  <div class="contact-band">
    <svg width="516" height="25" viewBox="0 0 516 25">
      <rect x="0" y="0" width="56" height="25" fill="#22c2c4"/>
      <polygon points="56,0 118,0 110,12.5 118,25 56,25" fill="#fff"/>
      <polygon points="70,2 80,2 72,12.5 80,23 70,23 62,12.5" fill="#22c2c4"/>
      <polygon points="86,2 96,2 88,12.5 96,23 86,23 78,12.5" fill="#22c2c4"/>
      <polygon points="102,2 112,2 104,12.5 112,23 102,23 94,12.5" fill="#22c2c4"/>
      <polygon points="120,0 516,0 516,25 120,25 112,12.5" fill="#1b3a8c"/>
    </svg>
    <div class="contact-list">
      <svg class="ico" width="11" height="8" viewBox="0 0 11 8"><rect width="11" height="8" rx="1" fill="#fff"/><path d="M0.5 0.8 L5.5 4.6 L10.5 0.8" stroke="#1b3a8c" stroke-width="1.1" fill="none"/></svg>
      <span>claire.moreau@northbound-mail.com</span>
      <svg class="ico" width="8" height="8" viewBox="0 0 8 8"><circle cx="4" cy="4" r="4" fill="#fff"/></svg>
      <span class="strong">555 210 0148</span>
      <svg class="ico" width="8" height="8" viewBox="0 0 8 8"><rect width="8" height="8" rx="1" fill="#fff"/></svg>
      <span>www.proflink.net/claire-moreau</span>
    </div>
  </div>

  <p class="copy" style="top:140px"><span class="lead-name">Claire Moreau</span> helps companies tackle and succeed in making change by providing project leadership and program management services for key business objectives.&nbsp; She understands the importance of getting it right the first time, and specializes in shaping solutions to drive complex business initiatives from strategy to action.</p>

  <h2 class="section-title" style="top:210px">Expertise and Capabilities:</h2>

  <table class="capabilities">
    <tr>
      <td class="area">Mergers and<br>Acquisitions</td>
      <td><ul class="emph">
        <li>For companies acquiring a target: Build integration teams, lead team in developing integration plan &amp; budget, facilitate planning for an efficient and effective Day 1, and for 30-60-90 day horizon</li>
        <li>Assist companies looking to be acquired to prepare their people, processes and systems for due diligence</li>
      </ul></td>
    </tr>
    <tr>
      <td class="area">Inflation Reduction Act</td>
      <td><ul>
        <li>Drug price negotiation operational readiness: Put in place process and governance for submission development and ensuing engagements with CMS. Identify cross-functional team members needed, design approval processes, build and oversee integrated project plan and timeline.</li>
        <li>Part D redesign readiness: Identify gaps and develop plan to address, including chartering workstreams and creation and implementation of plans and timelines to drive from strategy to execution</li>
      </ul></td>
    </tr>
    <tr>
      <td class="area">Strategic Programs &amp;<br>Business Transformation</td>
      <td><ul>
        <li>Develop strategy, framework and governance to accomplish organization and business model change, inclusive of people, processes and systems</li>
        <li>Change Management for new ways of working and new business models</li>
        <li>Facilitate goal-setting and strategic prioritization exercises with leadership teams</li>
      </ul></td>
    </tr>
  </table>

  <svg class="foot-band" width="516" height="12" viewBox="0 0 516 12">
    <polygon points="0,0 402,0 408,12 0,12" fill="#1b3a8c"/>
    <polygon points="412,0 424,0 430,12 418,12" fill="#22c2c4"/>
    <polygon points="430,0 442,0 448,12 436,12" fill="#22c2c4"/>
    <polygon points="448,0 460,0 466,12 454,12" fill="#22c2c4"/>
    <polygon points="466,0 516,0 516,12 472,12" fill="#22c2c4"/>
  </svg>
</section>

<!-- Page 2 -->
<section class="page page--two">
  <div class="brand"><span class="brand__mark"></span><div class="brand__name"><span>NORTHBOUND</span><span>ADVISORY LLC</span></div></div>
  <div class="identity">
    <div class="identity__name">Claire Moreau</div>
    <div class="identity__role">INDEPENDENT CONSULTANT</div>
    <ul class="identity__claims"><li>Solving Complex Challenges</li><li>Driving Programs from Strategy to Action</li></ul>
  </div>
  <div class="contact-band">
    <svg width="516" height="25" viewBox="0 0 516 25">
      <rect x="0" y="0" width="56" height="25" fill="#22c2c4"/>
      <polygon points="56,0 118,0 110,12.5 118,25 56,25" fill="#fff"/>
      <polygon points="70,2 80,2 72,12.5 80,23 70,23 62,12.5" fill="#22c2c4"/>
      <polygon points="86,2 96,2 88,12.5 96,23 86,23 78,12.5" fill="#22c2c4"/>
      <polygon points="102,2 112,2 104,12.5 112,23 102,23 94,12.5" fill="#22c2c4"/>
      <polygon points="120,0 516,0 516,25 120,25 112,12.5" fill="#1b3a8c"/>
    </svg>
    <div class="contact-list">
      <svg class="ico" width="11" height="8" viewBox="0 0 11 8"><rect width="11" height="8" rx="1" fill="#fff"/><path d="M0.5 0.8 L5.5 4.6 L10.5 0.8" stroke="#1b3a8c" stroke-width="1.1" fill="none"/></svg>
      <span>claire.moreau@northbound-mail.com</span>
      <svg class="ico" width="8" height="8" viewBox="0 0 8 8"><circle cx="4" cy="4" r="4" fill="#fff"/></svg>
      <span class="strong">555 210 0148</span>
      <svg class="ico" width="8" height="8" viewBox="0 0 8 8"><rect width="8" height="8" rx="1" fill="#fff"/></svg>
      <span>www.proflink.net/claire-moreau</span>
    </div>
  </div>

  <h2 class="about-title">About Claire Moreau:</h2>
  <div class="portrait" role="img" aria-label="Portrait photograph of Claire Moreau"></div>
  <p class="about-intro">As a passionate executive with 25 years of Pharmaceutical and MedTech expertise at Halvorsen Health, Claire is now helping companies achieve business results by providing leadership and oversight for key objectives and initiatives.&nbsp; She brings clarity to the complex and pioneers the way forward to solve new problems, leading critical business programs to rapid and seamless execution.</p>

  <div class="about-more">
    <p>Ms. Moreau is known for uncovering new solutions, connecting the dots, building strong cross-functional relationships, and driving engagement across teams.</p>
    <p>Claire leverages her robust marketing background to enhance strategic transformations by infusing customer-centric insights, effective communication, and commercial focus.&nbsp; Her marketing roles included product development and launch, global portfolio management, managing alliances for innovative external partnerships and KOL development.</p>
    <p>Ms. Moreau is a dual citizen of France and the US, and has lived and worked on two continents. She leverages her cross-cultural know-how to advance business collaboration and business goals.</p>
  </div>

  <div class="achievements">
    <h3 class="achievements__title">Claire has held leadership roles in Marketing, M&amp;A, Business Transformation and Strategy &amp; Operations. Her achievements include:</h3>
    <ul>
      <li><span class="key">Directed enterprise-wide integration team</span> accountable for integrating a foot &amp; ankle implants company into Halvorsen: transitioned from distributors to direct sales force, doubled production, met quality remediation goals, orchestrated organizational structure &amp; technology changes, and moved customer service and distribution.</li>
      <li><span class="key">Led integration</span> and new business model implementation of a critical asset in the Joint Reconstruction space that resulted in increased product pull-through, exceeding deal model expectations by double digits</li>
      <li>Drove business readiness and company response to the unprecedented changes stemming from the <span class="key">Inflation Reduction Act</span>. Led operations for 2 drug price negotiation submissions to CMS. Created and facilitated program of 6 workstreams, leading IRA transformation activities.</li>
      <li><span class="key">Strategy &amp; Ops lead for launch</span> of company’s first CAR-T cell therapy. Dove in deep with a series of workshops to define launch plan and interdependencies, designed and implemented team structure and project governance, navigated changing landscape and unforeseen challenges, resulting in a best-in-class launch that has become a role model in the cell and gene therapy space.</li>
      <li><span class="key">As Strategic Business Transformation</span> lead for US Oncology business, orchestrated strategy and operations excellence, including business goal-setting, strategic planning process, leadership business reviews and oversight of launch planning for 5 new drugs.</li>
    </ul>
  </div>

  <svg class="foot-band" width="516" height="12" viewBox="0 0 516 12">
    <polygon points="0,0 402,0 408,12 0,12" fill="#1b3a8c"/>
    <polygon points="412,0 424,0 430,12 418,12" fill="#22c2c4"/>
    <polygon points="430,0 442,0 448,12 436,12" fill="#22c2c4"/>
    <polygon points="448,0 460,0 466,12 454,12" fill="#22c2c4"/>
    <polygon points="466,0 516,0 516,12 472,12" fill="#22c2c4"/>
  </svg>
</section>

</body>
</html>
```